Velmar Ops Business Cards

We need to design some upbeat business cards. We are an Industrial Rope Access Company/Height Safety Company that specialize in Rope Access, Confined Space, Anchor Points, Safety Systems, PPE Inspecions and Rigging.
Company name is Velmar Ops Ltd
Card is for Gareth Lomas the Company Director
His mobile number is 027 418 9072 and email is gareth@velmarops.co.nz. Website address is www.velmarops.co.nz.
We will post some pictures below to ensure you get a good idea of what we do.

```html
<!DOCTYPE html>
<html lang="en">
<head>
<meta charset="utf-8">
<title>Velmar Ops Business Cards</title>
<link href="https://fonts.googleapis.com/css2?family=Lato:wght@400;900&family=Oswald:wght@600&display=swap" rel="stylesheet">
<style>
  :root {
    --brand-blue: #2c4596;
    --brand-blue-light: #4560ad;
    --paper: #ffffff;
    --ink: #3a3a3a;
    --backdrop: #e4e4e4;
  }
  * { box-sizing: border-box; margin: 0; padding: 0; }
  html, body {
    width: 1200px;
    height: 913px;
    overflow: hidden;
    background: var(--backdrop);
  }
  .canvas {
    position: relative;
    width: 1200px;
    height: 913px;
    display: flex;
    align-items: center;
    justify-content: center;
    gap: 50px;
  }
  .card {
    position: relative;
    width: 540px;
    height: 327px;
    box-shadow: 0 6px 18px rgba(0,0,0,0.15);
  }
  .card--front {
    background: radial-gradient(ellipse at 55% 40%, var(--brand-blue-light) 0%, var(--brand-blue) 70%);
    display: flex;
    flex-direction: column;
    align-items: center;
    justify-content: center;
    color: var(--paper);
  }
  .wordmark {
    font-family: "Lato", sans-serif;
    font-weight: 900;
    letter-spacing: 1px;
    line-height: 1;
  }
  .card--front .wordmark {
    font-size: 58px;
    color: var(--paper);
    margin-top: -10px;
  }
  .card--front .website {
    font-family: "Lato", sans-serif;
    font-weight: 400;
    font-size: 15px;
    letter-spacing: 1.5px;
    margin-top: 26px;
  }
  .card--back {
    background: var(--paper);
  }
  .card--back .wordmark {
    position: absolute;
    top: 44px;
    right: 34px;
    font-size: 44px;
    color: var(--brand-blue);
  }
  .contact-block {
    position: absolute;
    left: 40px;
    bottom: 38px;
    font-family: "Lato", sans-serif;
    color: var(--ink);
  }
  .person-name {
    font-family: "Oswald", sans-serif;
    font-weight: 600;
    font-size: 24px;
    letter-spacing: 0.5px;
    text-transform: uppercase;
    color: var(--brand-blue);
    line-height: 1.1;
  }
  .person-role {
    font-size: 15px;
    margin-top: 2px;
  }
  .divider {
    width: 30px;
    height: 1px;
    background: var(--ink);
    margin: 14px 0 12px;
  }
  .contact-line {
    font-size: 15px;
    line-height: 1.5;
    letter-spacing: 0.3px;
  }
  .contact-line .sep { margin: 0 8px; }
</style>
</head>
<body>
  <main class="canvas">
    <section class="card card--front" aria-label="Card front">
      <div class="wordmark">Velmar Ops</div>
      <div class="website">www.velmarops.co.nz</div>
    </section>

    <section class="card card--back" aria-label="Card back">
      <div class="wordmark">Velmar Ops</div>
      <div class="contact-block">
        <div class="person-name">Gareth Lomas</div>
        <div class="person-role">Director</div>
        <div class="divider"></div>
        <div class="contact-line">027 418 9072<span class="sep">|</span>gareth@velmarops.co.nz</div>
        <div class="contact-line">www.velmarops.co.nz</div>
      </div>
    </section>
  </main>
</body>
</html>
```